Modern Billboard Ad for Criminal Defense Firm

10.5 x 36 We're looking for something to set us apart from the local competition. Looking for sleek and modern. We're a mid-sized firm in a small market city. We want to give the artist room to be creative on this one.
Thanks

Target Market(s)

Adult clients who have been charged with a crime/DWI

Industry/Entity Type

legal

Font styles to use
Serif
Sans Serif

Requirements
Must have
• Needs to have the firm name in large lettering. Law Offices of Marcus T Whitfield. “PLLC” does not have to be included. Phone number of (555) 384-1927 should be included but not the main focus.
Nice to have
• A call to action or something similar. “Don’t go it alone, call today.”, “ Arrested?”

```html
<!DOCTYPE html>
<html lang="en">
<head>
<meta charset="utf-8">
<title>Law Office of Marcus T Whitfield – Billboard</title>
<link rel="stylesheet" href="https://fonts.googleapis.com/css2?family=Montserrat:ital,wght@0,700;0,800;1,400&family=Montserrat+Alternates:wght@500&display=swap">
<style>
  :root {
    --page: #1c1c1c;
    --board: #2f2f2f;
    --brick-dark: #3a3a3a;
    --brick-light: #6b6b6b;
    --title-fill: #e4e4e6;
    --title-stroke: #1b86b8;
    --rule: #e8a317;
    --tagline: #d2d2d2;
    --gold: #d9ac14;
    --badge: #2a2a2a;
    --badge-ring: #9a9a9a;
  }
  html, body {
    margin: 0;
    width: 1200px;
    height: 488px;
    overflow: hidden;
    background: var(--page);
  }
  .billboard {
    position: absolute;
    left: 20px;
    top: 75px;
    width: 1160px;
    height: 338px;
  }
  .title {
    font-family: "Montserrat", sans-serif;
    font-weight: 800;
    font-size: 78px;
    fill: var(--title-fill);
    stroke: var(--title-stroke);
    stroke-width: 5px;
    paint-order: stroke;
    letter-spacing: 1px;
  }
  .name {
    font-family: "Montserrat Alternates", sans-serif;
    font-weight: 500;
    font-size: 70px;
    fill: var(--title-fill);
    stroke: var(--title-stroke);
    stroke-width: 5px;
    paint-order: stroke;
  }
  .tagline {
    font-family: "Montserrat", sans-serif;
    font-style: italic;
    font-weight: 400;
    font-size: 24px;
    fill: var(--tagline);
    letter-spacing: 1px;
  }
  .phone-number {
    font-family: "Montserrat", sans-serif;
    font-weight: 700;
    font-size: 36px;
    fill: var(--gold);
    letter-spacing: 1px;
  }
</style>
</head>
<body>
<svg class="billboard" viewBox="0 0 1160 338" xmlns="http://www.w3.org/2000/svg">
  <defs>
    <linearGradient id="brick-corner" x1="0" y1="0" x2="1" y2="1">
      <stop offset="0" stop-color="var(--brick-light)"/>
      <stop offset="1" stop-color="var(--brick-dark)"/>
    </linearGradient>
    <linearGradient id="portrait-tone" x1="0" y1="0" x2="1" y2="1">
      <stop offset="0" stop-color="#6e6e6e"/>
      <stop offset="0.6" stop-color="#8a8a8a"/>
      <stop offset="1" stop-color="#5a5a5a"/>
    </linearGradient>
  </defs>

  <rect class="board" width="1160" height="338" fill="var(--board)"/>

  <path class="brick-corner" role="img" aria-label="Angled grey brick wall texture"
        d="M0 0 H200 C215 20 190 60 210 90 C230 130 200 170 220 210 C235 250 210 300 230 338 H0 Z"
        fill="url(#brick-corner)" opacity="0.55"/>

  <path class="portrait" role="img" aria-label="Black and white photo of the attorney in a vest and tie, jacket over his shoulder, in front of a brick wall"
        d="M790 0 H1160 V338 H820 C805 300 830 260 812 220 C795 180 822 140 800 100 C785 60 810 30 790 0 Z"
        fill="url(#portrait-tone)"/>

  <text class="title" x="45" y="85">LAW OFFICE OF</text>
  <text class="name" x="45" y="148">Marcus T Whitfield</text>

  <rect class="rule" x="45" y="168" width="652" height="3" fill="var(--rule)"/>

  <text class="tagline" x="53" y="211">‘Don't do it alone, call today.’, ’Arrested?’</text>

  <g class="phone-badge">
    <circle cx="84" cy="287" r="36" fill="var(--badge)" stroke="var(--badge-ring)" stroke-width="3"/>
    <path d="M70 270 l8 -3 l6 12 l-5 4 c3 7 8 12 15 15 l4 -5 l12 6 l-3 8 c-2 3 -6 4 -10 3 c-14 -4 -26 -16 -30 -30 c-1 -4 0 -8 3 -10 z"
          fill="var(--gold)"/>
  </g>
  <text class="phone-number" x="159" y="301">(555) 384-1927</text>
</svg>
</body>
</html>
```